Coldforge Prime manufacturing Project

We are looking at getting a brand new design for a new company that deals in selling stainless tubing and other stainless still products such as handrails, Spigots, Balustrade Fittings
Glass, Glass fittings and Aluminium Channels

We require a very clean website that deals with the following colours:

Blue to light blues
Blacks
Greys to light Greys
Whites

We are open for other ideas BUT we *DO NOT* want any pinks, greens or bright colours except for backgrounds colours we have chosen above. (It can be solid, gradient or a subtle pattern)

YOU MUST KEEP THE LOGO AS IS. PLEASE DO NOT ALTER THE LOGO IN *ANY WAY* and the logo MUST be the same colours and fonts.

Logo is attached.

The site must contain these aspects:
jQuery Slider (Image slide show)
Top drop down Menus
Be no more than 900px wide
Text is to be to the w3C standards. (no special fonts)

We will chop up the design into html format. You just need to provide the PSD file.

The clients opposition is:
www.quorvatrim.example

Industry/Entity Type

It Company

Requirements
Nice to have
• Alter the logo in anyway

Files

```html
<!DOCTYPE html>
<html lang="en">
<head>
<meta charset="utf-8">
<title>Coldforge Prime Manufacturing Co. Ltd</title>
<link href="https://fonts.googleapis.com/css2?family=Arimo:wght@400;700&family=Crimson+Pro:wght@500&display=swap" rel="stylesheet">
<style>
:root{
  --page:#ebebeb;
  --panel:#ffffff;
  --band:#dedede;
  --ink:#333333;
  --ink-soft:#555555;
  --nav-ink:#7c7c7c;
  --line:#c8c8c8;
  --steel-dark:#6e7378;
  --steel-light:#e6e8ea;
}
*{box-sizing:border-box;margin:0;padding:0}
html,body{width:1200px;height:1049px;overflow:hidden;background:var(--page)}
body{position:relative;font-family:"Arimo",Arial,sans-serif;color:var(--ink)}
.abs{position:absolute}

.brand-mark{left:102px;top:58px;width:174px;height:174px;border-radius:50%;
  background:radial-gradient(circle at 50% 40%,#fafafa,#d4d4d4);border:1px solid #cfcfcf;
  box-shadow:0 2px 6px rgba(0,0,0,.15);z-index:3}
.brand-name{left:269px;top:58px;font-family:"Crimson Pro",Georgia,serif;font-weight:500;font-size:31px;color:#2c2c2c}
.brand-sub{left:291px;top:94px;font-family:"Crimson Pro",Georgia,serif;font-weight:500;font-size:15px;letter-spacing:3px;color:#2c2c2c}

.search{left:870px;top:80px;width:204px;height:31px;border:1px solid #bdbdbd;border-radius:16px 0 0 16px;
  background:linear-gradient(#f3f3f3,#ffffff);display:flex;align-items:center;padding-left:17px;font-size:14px;color:#666}
.search-btn{position:absolute;right:0;top:0;width:31px;height:29px;background:linear-gradient(#e2e2e2,#c9c9c9);display:flex;align-items:center;justify-content:center}

.nav{left:275px;top:121px;width:799px;height:50px;background:linear-gradient(#f7f7f7,#e2e2e2);
  border:1px solid #cfcfcf;border-left:none;box-shadow:inset 0 -3px 0 #fff;display:flex;align-items:center;padding-left:32px}
.nav a{font-weight:700;font-size:16.5px;color:var(--nav-ink);text-decoration:none;letter-spacing:.3px}
.nav .dot{width:5px;height:5px;border-radius:50%;background:#999;margin:0 30px}

.hero{left:119px;top:172px;width:955px;height:319px;background:var(--panel)}
.slide-photo{left:370px;top:70px;width:270px;height:250px;border-radius:40% 40% 10% 10%;
  background:radial-gradient(circle at 55% 40%,#d6d9dc,#9da3a8 55%,#ffffff 90%)}
.slide-title{left:69px;top:126px;font-size:23px;line-height:27px}
.slide-title b{font-weight:700}
.arrow{top:134px}
.dots{left:311px;top:272px;display:flex;gap:7px}
.dots span{width:14px;height:14px;border-radius:50%;border:1px solid #bbb;background:#f4f4f4}
.dots .on{background:radial-gradient(#333 35%,#f4f4f4 40%)}

.intro{left:681px;top:0;width:274px;height:319px;border-left:1px solid #e2e2e2;padding:12px 12px 0 12px}
.intro h2{font-size:23px;font-weight:700;color:var(--ink)}
.intro h2 small{font-size:13px;font-weight:400}
.intro .lead{font-size:13px;line-height:18px;margin-top:-2px}
.intro h3{font-size:22px;font-weight:700;margin-top:20px;margin-bottom:4px}
.intro p{font-size:12.6px;line-height:18.2px;color:var(--ink)}
.btn{display:inline-flex;align-items:center;justify-content:center;border-radius:14px;
  background:linear-gradient(#fafafa,#d2d2d2);border:1px solid #c4c4c4;box-shadow:0 2px 2px rgba(0,0,0,.2);
  font-weight:700;font-size:14px;color:var(--ink)}
.intro .btn{margin-top:26px;width:110px;height:27px}

.products-band{left:119px;top:493px;width:955px;height:84px;background:var(--band)}
.products-band h2{position:absolute;left:20px;top:20px;font-size:35px;font-weight:400;letter-spacing:-.3px}
.products-band h2 b{font-weight:700}
.next{position:absolute;right:14px;top:33px;font-weight:700;font-size:15px;display:flex;align-items:center;gap:3px}

.tiles{left:119px;top:577px;width:955px;height:242px;background:var(--band);padding:0 5px;display:flex;gap:2px}
.tile{flex:1;height:236px;border:1px solid #fff}
.t1{background:radial-gradient(circle at 40% 50%,#f2f3f4,#9aa0a6 45%,#ffffff 75%)}
.t2{background:linear-gradient(100deg,#f6f6f6,#dfe2e4 40%,#f2f2f2 70%,#d8dadb)}
.t3{background:linear-gradient(135deg,#b7b9ba,#7c8083 50%,#eeeeee 90%)}
.t4{background:radial-gradient(circle at 70% 55%,#c8ccd0,#8d9297 40%,#ffffff 70%)}

.new-band{left:119px;top:819px;width:955px;height:143px;background:var(--panel)}
.new-title{position:absolute;left:22px;top:48px;display:flex;align-items:center;gap:10px;font-size:35px}
.new-title b{font-weight:700}
.new-photo{position:absolute;left:299px;top:0;width:656px;height:143px;
  background:linear-gradient(90deg,#1b1b1b,#6a6a6a 40%,#c9c9c9 60%,#3a3a3a 90%,#111)}
.new-photo .btn{position:absolute;left:431px;top:59px;width:180px;height:25px;border-radius:13px}

.footer{left:119px;top:964px;width:955px;height:29px;background:var(--band);font-size:13.5px;
  display:flex;align-items:center;justify-content:center;color:var(--ink)}
</style>
</head>
<body>
<header>
  <div class="abs brand-mark" aria-hidden="true"></div>
  <div class="abs brand-name">Coldforge Prime</div>
  <div class="abs brand-sub">Manufacturing Co. Ltd</div>
  <div class="abs search">Search
    <span class="search-btn"><svg width="18" height="18" viewBox="0 0 18 18"><circle cx="7.5" cy="7.5" r="5.5" fill="none" stroke="#555" stroke-width="2"/><line x1="11.5" y1="11.5" x2="16" y2="16" stroke="#555" stroke-width="2.2"/></svg></span>
  </div>
  <nav class="abs nav">
    <a>HOME</a><span class="dot"></span><a>ABOUT QUORVA</a><span class="dot"></span><a>PRODUCTS</a><span class="dot"></span><a>DOWNLOAD</a><span class="dot"></span><a>CONTACT</a>
  </nav>
</header>

<section class="abs hero">
  <div class="abs slide-photo" role="img" aria-label="Polished stainless glass clamp fitting with reflection"></div>
  <svg class="abs arrow" style="left:22px" width="22" height="42" viewBox="0 0 22 42"><polyline points="19,2 3,21 19,40" fill="none" stroke="#444" stroke-width="3"/></svg>
  <div class="abs slide-title"><b>The Solution For Complete</b><br>Glass Balustrade System</div>
  <svg class="abs arrow" style="left:624px" width="22" height="42" viewBox="0 0 22 42"><polyline points="3,2 19,21 3,40" fill="none" stroke="#444" stroke-width="3"/></svg>
  <div class="abs dots"><span></span><span class="on"></span><span></span></div>
  <aside class="abs intro">
    <h2>Welcome <small>to Coldforge Prime</small></h2>
    <div class="lead">Glass, Glass fittings and Aluminium Channels.</div>
    <h3>Who We are?</h3>
    <p>Lorem Ipsum is simply dummy text of the printing and typesetting industry. Lorem Ipsum has been the industry's standard dummy text ever since the 1500s, when an unknown printer took a galley of type and scrambled it to make a type specimen book.</p>
    <span class="btn">Read More</span>
  </aside>
</section>

<section class="abs products-band">
  <h2><b>Coldforge Prime</b> Products</h2>
  <div class="next">NEXT <svg width="18" height="18" viewBox="0 0 18 18"><polyline points="2,2 9,9 2,16" fill="none" stroke="#333" stroke-width="2"/><polyline points="9,2 16,9 9,16" fill="none" stroke="#333" stroke-width="2"/></svg></div>
</section>
<div class="abs tiles">
  <div class="tile t1" role="img" aria-label="Stainless steel pipe coupling"></div>
  <div class="tile t2" role="img" aria-label="Aluminium channel profiles"></div>
  <div class="tile t3" role="img" aria-label="Brushed aluminium U channel"></div>
  <div class="tile t4" role="img" aria-label="Stainless glass clamp fitting"></div>
</div>

<section class="abs new-band">
  <div class="new-title"><svg width="30" height="30" viewBox="0 0 30 30"><circle cx="15" cy="15" r="13.5" fill="none" stroke="#333" stroke-width="1.6"/><polyline points="12,9 18,15 12,21" fill="none" stroke="#333" stroke-width="1.8"/></svg><span><b>New</b> Products</span></div>
  <div class="new-photo" role="img" aria-label="Black and white interior of a modern building atrium with glass balustrades">
    <span class="btn">Download Catalogue</span>
  </div>
</section>

<footer class="abs footer">Copyright © Coldforge Prime Manufacturing Co. Ltd. All Rights Reserved.</footer>
</body>
</html>
```